Whitcombe Framing Works - Card Design

I am looking to use the logo designs that you already did for me to develop a business card. I would like the card to have a black background and be double sided. I want white and green logo and text. I have attached an inspiration photo of a look that I like. I would like to use the Vertical Logo attached to take up the full front side of the card. On the back where I have my name and information, I would like to have the horizontal logo or maybe even just the image of the 'A' and trees without the text. I am open, but I am looking for something clean and simple and I want the green to really pop! Additional files can be found under Design #: 40593216

Target Market(s)

Homeowners

Industry/Entity Type

Construction

Contact Information for Business Card

Name: Marcus Pellow, Title: Project Manager, Phone: 831.555.0147, Email: whitcombeframingworks@mailbarn.net, address: 418 Juniper Ln, Felton, CA 95092, Lic# 2046318

Colors
00AB8E
00BBA5
67D7C9
C6EFE9
E9F9F6

Requirements
Nice to have
• I would like to see the logos that I have already got from SketchHarbor, though I am open to new ones

```html
<!DOCTYPE html>
<html lang="en">
<head>
<meta charset="utf-8">
<title>Whitcombe Framing Works – Business Card</title>
<link rel="stylesheet" href="https://fonts.googleapis.com/css2?family=Open+Sans:wght@400;700&display=swap">
<style>
  :root {
    --backdrop: #474747;
    --card-black: #151515;
    --brand-green: #6ab547;
    --edge-green: #3cb54a;
    --ink-white: #ffffff;
  }
  * { margin: 0; padding: 0; box-sizing: border-box; }
  html, body { width: 1200px; height: 801px; overflow: hidden; }
  body {
    background: var(--backdrop);
    font-family: "Open Sans", sans-serif;
    position: relative;
  }
  .card {
    position: absolute;
    width: 560px;
    height: 320px;
    background: var(--card-black);
    border-bottom: 3px solid var(--edge-green);
    border-left: 2px solid var(--edge-green);
    box-shadow: 0 12px 28px rgba(0,0,0,0.45);
    color: var(--ink-white);
  }
  .card--details { left: 30px; top: 110px; }
  .card--front { left: 610px; top: 370px; }

  /* details side */
  .company-name {
    position: absolute;
    right: 36px;
    top: 46px;
    display: flex;
    align-items: center;
    gap: 10px;
    font-weight: 700;
    font-size: 19px;
    letter-spacing: 0.5px;
    color: var(--ink-white);
  }
  .company-name__dot {
    width: 14px; height: 14px;
    border-radius: 50%;
    background: var(--brand-green);
  }
  .person {
    position: absolute;
    left: 36px;
    top: 118px;
  }
  .person__name {
    font-weight: 700;
    font-size: 27px;
    color: var(--brand-green);
    line-height: 1.15;
  }
  .person__title {
    font-size: 17px;
    line-height: 1.3;
  }
  .divider {
    position: absolute;
    left: 36px;
    right: 36px;
    top: 196px;
    height: 2px;
    background: var(--brand-green);
  }
  .contact {
    position: absolute;
    left: 36px;
    top: 214px;
    font-size: 15px;
    line-height: 1.75;
  }
  .contact__row { display: flex; align-items: center; gap: 8px; }
  .contact__icon { width: 13px; height: 13px; flex: none; }
  .address {
    position: absolute;
    right: 36px;
    top: 214px;
    text-align: right;
    font-size: 15px;
    line-height: 1.75;
  }

  /* front side */
  .front-name {
    position: absolute;
    inset: 0;
    display: flex;
    align-items: center;
    justify-content: center;
    gap: 14px;
    font-weight: 700;
    font-size: 30px;
    letter-spacing: 0.5px;
    color: var(--ink-white);
  }
  .front-name__dot {
    width: 22px; height: 22px;
    border-radius: 50%;
    background: var(--brand-green);
  }
</style>
</head>
<body>
  <section class="card card--details">
    <div class="company-name"><span class="company-name__dot"></span>Whitcombe Framing Works</div>
    <div class="person">
      <p class="person__name">Marcus Pellow</p>
      <p class="person__title">Project Manager</p>
    </div>
    <div class="divider"></div>
    <div class="contact">
      <p class="contact__row">
        <svg class="contact__icon" viewBox="0 0 16 16"><path fill="#6ab547" d="M3.5 1l3 3-1.8 1.8a9 9 0 0 0 5.5 5.5L12 9.5l3 3-2 2C6.5 14.5 1.5 9.5 1.5 3z"/></svg>
        831.555.0147
      </p>
      <p class="contact__row">
        <svg class="contact__icon" viewBox="0 0 16 16"><rect x="1" y="3" width="14" height="10" fill="#6ab547"/><path d="M1 3l7 6 7-6" fill="none" stroke="#151515" stroke-width="1.4"/></svg>
        whitcombeframingworks@mailbarn.net
      </p>
    </div>
    <div class="address">
      <p>418 Juniper Ln, Felton, CA 95092</p>
      <p>Lic # 2046318</p>
    </div>
  </section>

  <section class="card card--front">
    <div class="front-name"><span class="front-name__dot"></span>Whitcombe Framing Works</div>
  </section>
</body>
</html>
```